Womans Supplement Designs

Launching a Supplement company and need to get some initial designs created, I've attached our logo and the bottle type that I want the samples done one.

This project is for our Whey Protein we are starting with Vanilla, chocolate and strawberry banana

(ALL DESIGN VARIATIONS MUST BE A WHITE BOTTLE NOT BLACK)

(FOR DESIGN SAMPLES PLEASE USE THE SUPPLEMENT BOTTLE STYLE I PROVIDED)

Whoever is selected the winner I will have more work for you to complete the disigns for the rest of the products in the line, Just want to get this shake completed first

Target Market(s)

Women

Requirements
Must have
• Must have our current logo involved

the name of this product will be "KIVA LUM"

Must have this slogan,

ALL-IN-ONE PREMIUM PROTEIN NUTRITIONAL SHAKE FOR BLACK WOMEN

This is our meal replacement

the design should try to keep the same look and feel of the existing provided supplement images

we are starting with chocolate, vanilla and strawberry banana

this is for women and should look colorful and appeal to them
Should not have
• Do not use an image of a person or lady, don't want it branded to a person

```html
<!DOCTYPE html>
<html lang="en">
<head>
<meta charset="utf-8">
<title>KIVA LUM Protein Shake Jars</title>
<link rel="stylesheet" href="https://fonts.googleapis.com/css2?family=Oswald:wght@400;600&family=Raleway:wght@200;600&display=swap">
<style>
  :root {
    --canvas: #ffffff;
    --jar: #f7f7f7;
    --jar-edge: #dedede;
    --lid: #ffffff;
    --lid-edge: #d6d6d6;
    --lid-ridge: #ececec;
    --ink: #111111;
    --ink-soft: #555555;
    --white: #ffffff;
    --choc-dark: #4a2a1c;
    --choc-light: #8a5a3e;
    --van-dark: #b98a5a;
    --van-light: #f3ead8;
    --berry: #d8343a;
    --banana: #f0cf3a;
  }
  * { margin: 0; padding: 0; box-sizing: border-box; }
  html, body { width: 1200px; height: 849px; overflow: hidden; background: var(--canvas); }
  .canvas { position: relative; width: 1200px; height: 849px; }

  .jar { position: absolute; top: 222px; width: 300px; height: 440px; }
  .jar--chocolate { left: 55px; }
  .jar--vanilla { left: 450px; }
  .jar--strawberry { left: 845px; }
  .jar-shape { position: absolute; inset: 0; width: 300px; height: 440px; }
  .jar-body { fill: var(--jar); stroke: var(--jar-edge); stroke-width: 1.5; }
  .jar-lid { fill: var(--lid); stroke: var(--lid-edge); stroke-width: 1.5; }
  .jar-lid-ridge { stroke: var(--lid-ridge); stroke-width: 1; }

  .brand-mark {
    position: absolute; top: 48px; left: 50%; transform: translateX(-50%);
    width: 112px; height: 74px; background: var(--ink);
    display: flex; align-items: flex-end; justify-content: center; padding-bottom: 14px; text-align: center;
    color: var(--white); font: 600 8px/1.3 "Raleway", sans-serif; letter-spacing: 1.5px;
  }
  .product-name {
    position: absolute; top: 138px; width: 100%; text-align: center; white-space: nowrap;
    font: 200 46px/1 "Raleway", sans-serif; letter-spacing: 3px; color: var(--ink);
  }
  .flavour-art {
    position: absolute; top: 204px; left: 40px; width: 180px; height: 156px;
    border-radius: 40% 50% 30% 45%;
  }
  .flavour-art--chocolate { background: radial-gradient(circle at 55% 60%, var(--choc-light), var(--choc-dark) 55%, var(--van-light) 92%); }
  .flavour-art--vanilla { background: radial-gradient(circle at 50% 60%, var(--van-dark), var(--van-light) 75%); }
  .flavour-art--strawberry { background: radial-gradient(circle at 40% 65%, var(--berry), var(--banana) 60%, var(--van-light) 92%); }

  .facts {
    position: absolute; top: 230px; left: 236px; width: 32px; height: 116px;
    border: 1.5px solid var(--ink); border-radius: 16px;
    display: flex; flex-direction: column; justify-content: space-evenly; align-items: center;
  }
  .fact { text-align: center; }
  .fact-value { display: block; font: 600 12px/1 "Oswald", sans-serif; color: var(--ink); }
  .fact-unit { display: block; font: 400 4.5px/1.1 "Oswald", sans-serif; color: var(--ink-soft); letter-spacing: 0.3px; }

  .flavour-tag {
    position: absolute; top: 366px; left: 50%; transform: translateX(-50%);
    width: 164px; height: 26px; border-radius: 13px; background: var(--ink); color: var(--white);
    display: flex; align-items: center; justify-content: center; white-space: nowrap;
    font: 600 12px/1 "Oswald", sans-serif; letter-spacing: 0.5px; text-transform: uppercase;
  }
</style>
</head>
<body>
<main class="canvas">

  <section class="jar jar--chocolate">
    <svg class="jar-shape" viewBox="0 0 300 440" aria-hidden="true">
      <path class="jar-body" d="M42,38 H258 Q294,42 297,92 V392 Q297,428 262,434 H38 Q3,428 3,392 V92 Q6,42 42,38 Z"/>
      <rect class="jar-lid" x="18" y="2" width="264" height="38" rx="6"/>
      <line class="jar-lid-ridge" x1="20" y1="12" x2="280" y2="12"/>
      <line class="jar-lid-ridge" x1="20" y1="30" x2="280" y2="30"/>
    </svg>
    <div class="brand-mark">EBONLANE<br>LIVING</div>
    <h1 class="product-name">KIVA LUM</h1>
    <div class="flavour-art flavour-art--chocolate" role="img" aria-label="Chocolate pieces with a milk splash"></div>
    <div class="facts">
      <div class="fact"><span class="fact-value">50</span><span class="fact-unit">SERVINGS</span></div>
      <div class="fact"><span class="fact-value">27</span><span class="fact-unit">PROTEIN<br>GRAMS</span></div>
      <div class="fact"><span class="fact-value">500</span><span class="fact-unit">CALORIES</span></div>
    </div>
    <div class="flavour-tag">Chocolate</div>
  </section>

  <section class="jar jar--vanilla">
    <svg class="jar-shape" viewBox="0 0 300 440" aria-hidden="true">
      <path class="jar-body" d="M42,38 H258 Q294,42 297,92 V392 Q297,428 262,434 H38 Q3,428 3,392 V92 Q6,42 42,38 Z"/>
      <rect class="jar-lid" x="18" y="2" width="264" height="38" rx="6"/>
      <line class="jar-lid-ridge" x1="20" y1="12" x2="280" y2="12"/>
      <line class="jar-lid-ridge" x1="20" y1="30" x2="280" y2="30"/>
    </svg>
    <div class="brand-mark">EBONLANE<br>LIVING</div>
    <h1 class="product-name">KIVA LUM</h1>
    <div class="flavour-art flavour-art--vanilla" role="img" aria-label="Vanilla pods, cinnamon sticks and flowers with a milk splash"></div>
    <div class="facts">
      <div class="fact"><span class="fact-value">50</span><span class="fact-unit">SERVINGS</span></div>
      <div class="fact"><span class="fact-value">27</span><span class="fact-unit">PROTEIN<br>GRAMS</span></div>
      <div class="fact"><span class="fact-value">500</span><span class="fact-unit">CALORIES</span></div>
    </div>
    <div class="flavour-tag">Vanila</div>
  </section>

  <section class="jar jar--strawberry">
    <svg class="jar-shape" viewBox="0 0 300 440" aria-hidden="true">
      <path class="jar-body" d="M42,38 H258 Q294,42 297,92 V392 Q297,428 262,434 H38 Q3,428 3,392 V92 Q6,42 42,38 Z"/>
      <rect class="jar-lid" x="18" y="2" width="264" height="38" rx="6"/>
      <line class="jar-lid-ridge" x1="20" y1="12" x2="280" y2="12"/>
      <line class="jar-lid-ridge" x1="20" y1="30" x2="280" y2="30"/>
    </svg>
    <div class="brand-mark">EBONLANE<br>LIVING</div>
    <h1 class="product-name">KIVA LUM</h1>
    <div class="flavour-art flavour-art--strawberry" role="img" aria-label="Strawberries and banana slices with a milk splash"></div>
    <div class="facts">
      <div class="fact"><span class="fact-value">50</span><span class="fact-unit">SERVINGS</span></div>
      <div class="fact"><span class="fact-value">27</span><span class="fact-unit">PROTEIN<br>GRAMS</span></div>
      <div class="fact"><span class="fact-value">500</span><span class="fact-unit">CALORIES</span></div>
    </div>
    <div class="flavour-tag">Strawberry Banana</div>
  </section>

</main>
</body>
</html>
```